Tera Vox

Graphic design for web pages depicting an environmental solution to human waste streams of plastic, tyres and bio mass, converting waste to energy. Technology used is a pyrolysis plant deconstructing 20tonnes per day of waste. Also touch up of logo

```html
<!DOCTYPE html>
<html lang="en">
<head>
<meta charset="utf-8">
<title>Tera Vox</title>
<link rel="stylesheet" href="https://fonts.googleapis.com/css2?family=Poppins:wght@400;500;600&family=Lora:wght@400;600&display=swap">
<style>
:root{
  --green:#62a843;
  --green-dark:#4f9333;
  --green-text:#5b9f3d;
  --green-pale:#dcebd5;
  --ink:#555a55;
  --white:#ffffff;
  --sand:#7a7f7a;
}
*{box-sizing:border-box;margin:0;padding:0}
html,body{width:1200px;height:4059px;overflow:hidden;background:var(--white);font-family:"Poppins",sans-serif;color:var(--ink)}
.page{position:relative;width:1200px;height:4059px}
.abs{position:absolute}
.top-bar{left:0;top:0;width:1200px;height:6px;background:var(--green)}
.brand{display:flex;flex-direction:column;align-items:center;gap:6px}
.brand-mark{width:40px;height:40px;background:#178f96}
.brand-name{font-family:"Poppins",sans-serif;font-weight:500;font-size:15px;color:#178f96;letter-spacing:.5px}
.header-brand{left:520px;top:50px;width:160px}
.nav{left:0;top:196px;width:1200px;height:44px;border-top:1.5px solid var(--green);border-bottom:1.5px solid var(--green)}
.nav a{position:absolute;top:0;height:41px;line-height:41px;font-size:15px;font-weight:500;color:var(--green-text);text-decoration:none;transform:translateX(-50%)}
.nav a.active{background:var(--green);color:var(--white);width:79px;text-align:center;transform:none}
.art{border-radius:48% 52% 45% 55%/55% 45% 55% 45%}
.hero-art{left:189px;top:347px;width:331px;height:281px;background:radial-gradient(circle at 50% 60%,#3f8d2c 0 30%,var(--green-pale) 31%)}
.hero-copy{left:600px;top:418px;width:425px;text-align:center;color:var(--green-text);font-size:24px;line-height:28px}
.hero-copy .dim{color:#6b6f6b}
.btn{display:block;background:var(--green);color:var(--white);text-align:center;font-weight:500;border-radius:7px;text-decoration:none}
.hero-btn{left:736px;top:501px;width:155px;height:51px;line-height:51px;font-size:17px}
.band{left:0;width:1200px;background:var(--green);color:var(--white)}
.section-title{position:absolute;left:189px;width:822px;text-align:center;font-family:"Lora",serif;font-weight:600;font-size:27px}
.rule{position:absolute;left:189px;width:822px;height:2px;background:var(--white)}
.rule.green{background:var(--green)}
.sol-icons{left:189px;top:975px;width:822px;height:150px}
.sol-label{position:absolute;top:1150px;font-size:15px;font-weight:600;transform:translateX(-50%);white-space:nowrap}
.sol-text{left:189px;top:1320px;width:475px;font-size:13px;line-height:19.5px;text-align:center}
.sol-art{left:718px;top:1274px;width:293px;height:271px;background:linear-gradient(160deg,#9bc98a,#7ab765)}
.who-art{left:189px;top:1782px;width:281px;height:260px;background:radial-gradient(circle at 45% 60%,#4d9a35 0 25%,var(--green-pale) 26%)}
.who-title{left:552px;top:1772px;width:458px;text-align:center;font-family:"Lora",serif;font-size:27px;color:#555}
.who-text{left:552px;top:1830px;width:458px;text-align:center;font-size:18px;line-height:24px;color:#6a6e6a}
.project{position:absolute;top:2384px;width:257px}
.project .photo{height:257px}
.project p{margin-top:27px;text-align:center;font-size:18px}
.blog-title{color:var(--green-text);top:2868px}
.post{position:absolute;left:186px;width:660px;height:147px}
.post .thumb{position:absolute;left:0;top:0;width:147px;height:147px;background:linear-gradient(90deg,#4a3e3c,#c9a49a 50%,#4a3e3c)}
.post .body{position:absolute;left:164px;top:0;width:496px}
.post h3{font-size:13px;font-weight:400;line-height:17px;color:#333}
.post .meta{font-size:8px;color:#777;margin-top:4px}
.post .excerpt{font-size:8px;line-height:12.5px;color:#777;margin-top:6px}
.post .more{font-size:9px;color:var(--green-text);margin-top:30px}
.blog-art{left:893px;top:2973px;width:298px;height:252px;background:linear-gradient(180deg,var(--green-pale),#a6d095)}
.blog-btn{left:527px;top:3331px;width:146px;height:41px;line-height:41px;font-size:13px;border-radius:2px}
.trust-title{color:var(--green-text);font-weight:400;top:3494px;font-size:23px}
.trust-band{left:0;top:3567px;width:1200px;height:257px;background:linear-gradient(180deg,#a59c9b 0%,#b8847a 35%,#3c5a70 55%,#23455c 100%)}
.stat{position:absolute;top:3632px;width:215px;height:129px;background:var(--white);text-align:center;font-family:"Lora",serif;font-weight:600;color:#333}
.stat .num{margin-top:20px;font-size:20px}
.stat .bar{width:128px;height:2px;background:var(--green);margin:19px auto 0}
.stat .label{margin-top:17px;font-size:17px}
.footer-brand{left:427px;top:3930px;width:160px}
.footer-btn{left:601px;top:3946px;width:153px;height:52px;line-height:52px;font-size:16px}
</style>
</head>
<body>
<div class="page">
  <div class="abs top-bar"></div>

  <div class="abs brand header-brand">
    <span class="brand-mark"></span>
    <span class="brand-name">Tera Vox</span>
  </div>

  <nav class="abs nav">
    <a class="active" href="#" style="left:186px">Home</a>
    <a href="#" style="left:372px">Solutions</a>
    <a href="#" style="left:533px">About Us</a>
    <a href="#" style="left:689px">Projects</a>
    <a href="#" style="left:825px">Blog</a>
    <a href="#" style="left:962px">Contact</a>
  </nav>

  <div class="abs art hero-art" role="img" aria-label="Illustration of a half globe with a smoking factory and wind turbines"></div>
  <div class="abs hero-copy">
    <p>Stop wasting <span class="dim">our</span> planet's <span class="dim">time...</span></p>
    <p>Let's start recycling our wastes</p>
  </div>
  <a class="abs btn hero-btn" href="#">Join Us</a>

  <section class="abs band" style="top:771px;height:861px">
    <h2 class="section-title" style="top:33px">Our Solutions</h2>
    <div class="rule" style="top:101px"></div>
    <div class="rule" style="top:461px"></div>
  </section>

  <svg class="abs sol-icons" viewBox="0 0 822 150" fill="none" stroke="#fff" stroke-width="6" stroke-linecap="round" stroke-linejoin="round">
    <g>
      <ellipse cx="50" cy="73" rx="45" ry="62"/>
      <ellipse cx="58" cy="73" rx="28" ry="48"/>
      <ellipse cx="62" cy="73" rx="12" ry="30"/>
    </g>
    <path d="M148 73h36M166 55v36"/>
    <g>
      <path d="M240 30a55 55 0 0 1 78 10M318 40l4-14M318 40l-14-2"/>
      <path d="M325 100a55 55 0 0 1-70 24M255 124l-14 2M255 124l2-14"/>
      <path d="M222 100a55 55 0 0 1 0-55"/>
      <rect x="265" y="45" width="30" height="70" rx="8"/>
      <path d="M272 45v-12h16v12M265 70h30M265 90h30"/>
    </g>
    <path d="M400 73h36M418 55v36"/>
    <g>
      <path d="M530 45c-20-12-50-5-50 35 0 35 25 65 40 60 8-3 12-3 20 0 15 5 40-25 40-60 0-40-30-47-50-35z"/>
      <path d="M530 45c0-15 8-25 20-30"/>
    </g>
    <path d="M628 62h34M628 84h34"/>
    <path d="M728 10l-36 65h42l-28 65 64-85h-40l36-45z"/>
  </svg>
  <span class="abs sol-label" style="left:239px;color:#fff">Tires Recycling</span>
  <span class="abs sol-label" style="left:479px;color:#fff">Plastic Recycling</span>
  <span class="abs sol-label" style="left:720px;color:#fff">Compost Recycling</span>
  <span class="abs sol-label" style="left:950px;color:#fff">Energy</span>

  <p class="abs sol-text" style="color:#fff">Lorem ipsum dolor sit amet, consectetur adipisicing elit, sed do eiusmod tempor incididunt ut labore et dolore magna aliqua. Ut enim ad minim veniam, quis nostrud exercitation ullamco laboris nisi ut aliquip ex ea commodo consequat. Duis aute irure dolor in reprehenderit in voluptate velit esse cillum dolore eu fugiat nulla pariatur. Excepteur sint occaecat cupidatat non proident, sunt in culpa qui officia deserunt mollit anim id est laborum. Sed ut perspiciatis unde omnis iste natus error sit voluptatem doloremque laudantium, totam rem aperiam, eaque ipsa quae ab illo inventore veritatis et quasi architecto</p>
  <div class="abs art sol-art" role="img" aria-label="Illustration of a person sorting waste into two recycling bins"></div>

  <div class="abs art who-art" role="img" aria-label="Illustration of a hand holding a small globe with trees"></div>
  <h2 class="abs who-title">Who Are We</h2>
  <p class="abs who-text">Lorem ipsum dolor sit amet, consectetur adipisicing elit, sed do eiusmod tempor incididunt ut labore et dolore magna aliqua. Ut enim ad minim veniam, quis nostrud exercitation ullamco laboris nisi ut aliquip ex ea commodo consequat. Duis aute irure dolor in reprehenderit in voluptate velit esse cillum dolore eu fugiat nulla pariatur. Excepteur sint occaecat cupidatat non proident, sunt in culpa qui off</p>

  <section class="abs band" style="top:2230px;height:514px">
    <h2 class="section-title" style="top:36px">Related Projects</h2>
    <div class="rule" style="top:84px"></div>
  </section>
  <div class="project" style="left:189px">
    <div class="photo" role="img" aria-label="Photo of solar panels under a blue sky" style="background:linear-gradient(180deg,#3f7fc6,#a9cbe8 70%,#2c3a4a 85%)"></div>
    <p style="color:#fff">Solar Energy</p>
  </div>
  <div class="project" style="left:471px">
    <div class="photo" role="img" aria-label="Photo of wind turbines over a field at sunset" style="background:linear-gradient(180deg,#c06a4a,#f08a4a 45%,#f4b060 60%,#6b5a30 70%,#5a4a28)"></div>
    <p style="color:#fff">Eco Energy</p>
  </div>
  <div class="project" style="left:754px">
    <div class="photo" role="img" aria-label="Photo of power line towers at dusk" style="background:linear-gradient(180deg,#3d4a5a,#8a7a6a 60%,#c08a5a 80%,#2e2a28)"></div>
    <p style="color:#fff">Hydraulic Energy</p>
  </div>

  <h2 class="section-title blog-title" style="color:var(--green-text)">From The Blog</h2>
  <div class="rule green" style="top:2906px"></div>

  <article class="post" style="top:2969px">
    <div class="thumb" role="img" aria-label="Photo of a city street between tall buildings"></div>
    <div class="body">
      <h3>Lorem ipsum dolor sit amet, consectetur Lorem ipsum dolor sit sed do eiusmod tempor incididunt ut.</h3>
      <p class="meta">By Admin / Blog</p>
      <p class="excerpt">Lorem ipsum dolor sit amet, consectetur adipisicing elit, sed do eiusmod tempor incididunt ut labore et dolore magna aliqua. Ut enim ad minim veniam, quis nostrud exercitation ullamco laboris nisi ut aliquip ex ea commodo consequat.</p>
      <p class="more">Read More »</p>
    </div>
  </article>
  <article class="post" style="top:3141px">
    <div class="thumb" role="img" aria-label="Photo of a city street between tall buildings"></div>
    <div class="body">
      <h3>Lorem ipsum dolor sit amet, consectetur Lorem ipsum dolor sit sed do eiusmod tempor incididunt ut.</h3>
      <p class="meta">By Admin / Blog</p>
      <p class="excerpt">Lorem ipsum dolor sit amet, consectetur adipisicing elit, sed do eiusmod tempor incididunt ut labore et dolore magna aliqua. Ut enim ad minim veniam, quis nostrud exercitation ullamco laboris nisi ut aliquip ex ea commodo consequat.</p>
      <p class="more">Read More »</p>
    </div>
  </article>
  <div class="abs art blog-art" role="img" aria-label="Illustration of a gardener watering a young plant"></div>
  <a class="abs btn blog-btn" href="#">Browse Our Blog</a>

  <h2 class="section-title trust-title">Trust Our Process</h2>
  <div class="rule green" style="top:3529px;height:1.5px"></div>
  <div class="abs trust-band" role="img" aria-label="Photo of colourful waterfront houses"></div>
  <div class="stat" style="left:85px"><p class="num">5+</p><div class="bar"></div><p class="label">Years Of Experience</p></div>
  <div class="stat" style="left:358px"><p class="num">300+</p><div class="bar"></div><p class="label">Planted Trees</p></div>
  <div class="stat" style="left:626px"><p class="num">200K+</p><div class="bar"></div><p class="label">Tonnes Recycled</p></div>
  <div class="stat" style="left:900px"><p class="num">10000+ W</p><div class="bar"></div><p class="label">Energy Produced</p></div>

  <div class="abs brand footer-brand">
    <span class="brand-mark"></span>
    <span class="brand-name">Tera Vox</span>
  </div>
  <a class="abs btn footer-btn" href="#">Contact Us</a>
</div>
</body>
</html>
```